Business Card Design/Stationary Design

We would like designers to submit cool, hip business card designs (plus stationary designs) for a new, upstart software development company located in Toronto.
If you have any questions, please email us.
For inspiration on designs:
http://cardmuse.example/cool-business-cards/
http://layoutnotes.example/2008/05/36-cool-business-cards-you-should%E2%80%99ve-seen.html
http://gigharbor.example/general/18-smokin-hot-business-card-designs/

Card info:

Selvakumar (Selv) Nadarasan

Founder and CEO

47 Brindle Court, Suite 311

Toronto, ON M4K 2T8

Phone: 647-512-7730

Mobile: 416-273-5094

Fax: 647-512-7731

Email: selvakumar.nadarasan@mailbrook.example

www.quendrix.example
Updates

Hi everyone,

In terms of all the designs I have seen so far, here is what I like:

1.  I really like the "back" part of this design.  The "front" looks pretty decent as well, but for the "front", look at #2 on this list.  I like that.

http://www.pitchboard.example/image.aspx?imageLocation=1000_10001_2000_image.jpg&type=design300px&whiteLabelCustId=9999

2. "Side 1" of this I like, the front needs to be reworked.

http://www.pitchboard.example/image.aspx?imageLocation=1000_10002_2000_image.png&type=design300px&whiteLabelCustId=9999

3. http://www.pitchboard.example/image.aspx?imageLocation=1000_10003_2000_image.jpg&type=design300px&whiteLabelCustId=9999

4. http://www.pitchboard.example/image.aspx?imageLocation=1000_10004_2000_image.jpg&type=design300px&whiteLabelCustId=9999

Target Market(s)

We are focused on enterprise customers right now, so businesses with a long-term goal of also reaching out to the consumer market as well.

Industry/Entity Type

Software

Requirements
Must have
• Must look cool, ultra-modern, clean and eye-catching. Must incorporate our logo and the colors found in the logo.

```html
<!DOCTYPE html>
<html lang="en">
<head>
<meta charset="utf-8">
<title>Quendrix Business Card</title>
<link rel="stylesheet" href="https://fonts.googleapis.com/css2?family=Open+Sans:wght@700&family=PT+Sans:wght@400;700&display=swap">
<style>
  :root {
    --label-green: #5b7b36;
    --wordmark-green: #6c7f3a;
    --mark-green: #8cc043;
    --accent-lime: #c8dc2e;
    --accent-teal: #17b57a;
    --accent-leaf: #7ab136;
    --name-green: #9aab3a;
    --title-olive: #8a9a2e;
    --band-olive: #97a03e;
    --band-dark: #5d7b36;
    --card-white: #ffffff;
    --page-white: #ffffff;
    --text-white: #ffffff;
  }
  * { margin: 0; padding: 0; box-sizing: border-box; }
  html, body {
    width: 1200px;
    height: 1200px;
    overflow: hidden;
    background: var(--page-white);
  }
  .board {
    position: relative;
    width: 1200px;
    height: 1200px;
  }
  .side-label {
    position: absolute;
    left: 25px;
    font-family: "Open Sans", sans-serif;
    font-weight: 700;
    font-size: 66px;
    color: var(--label-green);
    letter-spacing: -1px;
  }
  .side-label--front { top: 272px; }
  .side-label--back { top: 788px; }

  .card {
    position: absolute;
    left: 303px;
    width: 842px;
    height: 482px;
    background: var(--card-white);
    box-shadow: 4px 6px 12px rgba(0,0,0,0.35);
    overflow: hidden;
    font-family: "PT Sans", sans-serif;
  }
  .card--front { top: 70px; }
  .card--back { top: 637px; }

  .front-disc {
    position: absolute;
    left: 400px;
    top: -130px;
    width: 600px;
    height: 600px;
    border-radius: 50%;
    background: linear-gradient(135deg, var(--accent-lime) 0%, var(--accent-teal) 50%, var(--accent-leaf) 100%);
  }
  .front-wordmark {
    position: absolute;
    left: 93px;
    top: 318px;
    font-size: 92px;
    font-weight: 400;
    line-height: 1;
    color: var(--wordmark-green);
  }

  .back-header {
    position: absolute;
    left: 0; top: 0;
    width: 100%;
    height: 183px;
  }
  .brand-dot {
    position: absolute;
    left: 34px;
    top: 64px;
    width: 86px;
    height: 86px;
    border-radius: 50%;
    background: var(--mark-green);
  }
  .brand-name {
    position: absolute;
    left: 140px;
    top: 80px;
    font-size: 58px;
    font-weight: 400;
    line-height: 1;
    color: var(--wordmark-green);
  }
  .holder {
    position: absolute;
    left: 483px;
    top: 105px;
  }
  .holder-name {
    font-size: 19px;
    color: var(--name-green);
    line-height: 1.1;
  }
  .holder-title {
    font-size: 15px;
    font-weight: 700;
    color: var(--title-olive);
    margin-top: 2px;
  }

  .contact-band {
    position: absolute;
    left: 0; top: 183px;
    width: 100%;
    height: 239px;
    background: var(--band-olive);
  }
  .contact-list {
    position: absolute;
    left: 483px;
    top: 18px;
    list-style: none;
    color: var(--text-white);
    font-size: 14.5px;
    font-weight: 700;
    line-height: 20px;
  }
  .contact-list li + li { margin-top: 20px; }
  .contact-list .address { line-height: 19px; }

  .web-band {
    position: absolute;
    left: 0; top: 422px;
    width: 100%;
    height: 60px;
    background: var(--band-dark);
  }
  .web-address {
    position: absolute;
    left: 483px;
    top: 19px;
    color: var(--text-white);
    font-size: 14.5px;
    font-weight: 700;
  }
</style>
</head>
<body>
<main class="board">
  <div class="side-label side-label--front">FRONT</div>
  <section class="card card--front" aria-label="Card front">
    <span class="front-disc" aria-hidden="true"></span>
    <div class="front-wordmark">Quendrix</div>
  </section>

  <div class="side-label side-label--back">BACK</div>
  <section class="card card--back" aria-label="Card back">
    <header class="back-header">
      <span class="brand-dot" aria-hidden="true"></span>
      <div class="brand-name">Quendrix</div>
      <div class="holder">
        <div class="holder-name">Selvakumar (Selv) Nadarasan</div>
        <div class="holder-title">Founder and CEO</div>
      </div>
    </header>
    <div class="contact-band">
      <ul class="contact-list">
        <li class="address">47 Brindle Court, Suite 311<br>Toronto, ON M4K 2T8</li>
        <li>Phone: 647-512-7730</li>
        <li>Mobile: 416-273-5094</li>
        <li>Fax: 647-512-7731</li>
        <li>Email: selvakumar.nadarasan@mailbrook.example</li>
      </ul>
    </div>
    <div class="web-band">
      <div class="web-address">www.quendrix.example</div>
    </div>
  </section>
</main>
</body>
</html>
```